Zo Fen smart screen Flyer design

Hi,

Please see attached file as I have done up a very very basic flyer just with the information that will need to be presented.

Please don't go with this as a format I would like, as I have no design skills at all.

I'm looking for something that is basic but professional looking capturing this information.
I would prefer if the symbols were changed so they were all consistent and the colour scheme worked together with the logo.

If you can use the picture of the screen provided as I will replace this once my product has its photoshoot.

Thanks!

```html
<!DOCTYPE html>
<html lang="en">
<head>
<meta charset="utf-8">
<title>Zo Fen Smart Screen Flyer</title>
<link rel="stylesheet" href="https://fonts.googleapis.com/css2?family=Montserrat:wght@300;500;700&display=swap">
<style>
  :root {
    --ink: #111111;
    --paper: #ffffff;
    --magenta: #cc3fe6;
    --cyan: #6ff0ee;
    --yellow: #f7da1e;
    --screen-dark: #0d1a14;
    --screen-green: #2f8a3e;
    --screen-glow: #e8d35a;
  }
  html, body {
    margin: 0;
    padding: 0;
    width: 927px;
    height: 1200px;
    overflow: hidden;
    background: var(--paper);
  }
  .flyer {
    position: relative;
    width: 927px;
    height: 1200px;
    font-family: "Montserrat", sans-serif;
    color: var(--ink);
    overflow: hidden;
  }
  .backdrop {
    position: absolute;
    inset: 0;
  }
  .brand-name {
    position: absolute;
    left: 114px;
    top: 78px;
    width: 320px;
    margin: 0;
    text-align: center;
    font-weight: 500;
    font-size: 56px;
    line-height: 1;
    color: var(--ink);
  }
  .intro {
    position: absolute;
    left: 40px;
    width: 403px;
    text-align: right;
    font-weight: 300;
    font-size: 24.5px;
    line-height: 29px;
    margin: 0;
  }
  .intro-outdoor { top: 634px; }
  .intro-indoor { top: 808px; }
  .feature {
    position: absolute;
    left: 523px;
    width: 360px;
    height: 96px;
  }
  .feature h2 {
    margin: 0;
    font-weight: 300;
    font-size: 21px;
    line-height: 26px;
  }
  .feature p {
    margin: 8px 0 0;
    width: 222px;
    font-weight: 500;
    font-size: 14.2px;
    line-height: 15.5px;
  }
  .feature-icon {
    position: absolute;
    left: 270px;
    top: 4px;
    width: 85px;
    height: 95px;
  }
  .quote {
    position: absolute;
    right: 52px;
    top: 1022px;
    text-align: right;
    font-size: 34px;
    line-height: 42px;
  }
  .quote strong { display: block; font-weight: 700; }
  .quote span { display: block; font-weight: 300; }
  .contact {
    position: absolute;
    top: 1136px;
    font-weight: 700;
    font-size: 19.5px;
    letter-spacing: 0.3px;
  }
  .contact-web { left: 145px; }
  .contact-mail { right: 52px; }
</style>
</head>
<body>
<main class="flyer">
  <svg class="backdrop" width="927" height="1200" viewBox="0 0 927 1200">
    <defs>
      <radialGradient id="screen-fill" cx="40%" cy="48%" r="65%">
        <stop offset="0" stop-color="var(--screen-glow)"/>
        <stop offset="0.35" stop-color="var(--screen-green)"/>
        <stop offset="1" stop-color="var(--screen-dark)"/>
      </radialGradient>
    </defs>
    <polygon class="band band-yellow" points="0,42 181,0 267,0 0,62" fill="var(--yellow)"/>
    <polygon class="band band-magenta" points="0,291 927,75 927,95 0,314" fill="var(--magenta)"/>
    <polygon class="band band-cyan" points="0,1116 927,906 927,927 0,1137" fill="var(--cyan)"/>
    <polygon class="band band-yellow" points="720,1200 927,1153 927,1173 808,1200" fill="var(--yellow)"/>
    <polygon class="product-screen" points="68,338 441,261 441,591 62,564" fill="url(#screen-fill)" stroke="#1a1a1a" stroke-width="3" role="img" aria-label="Product photo of a wall-mounted LED display screen showing a bright green and yellow abstract image"/>
  </svg>

  <h1 class="brand-name">Zo Fen</h1>

  <p class="intro intro-outdoor">Bring attention to your business with your own HD LED display. Our displays can be mounted outdoors on walls, roofs, fixed signs, trailer mounted etc.</p>
  <p class="intro intro-indoor">We also do indoor LED screens for shop fronts and display stands. All screens are custom built to your requirements including size, shape and even curved displays.</p>

  <section class="feature" style="top:209px">
    <h2>4G Capable</h2>
    <p>Change screen content with a click of the mouse anywhere in the world</p>
    <svg class="feature-icon" viewBox="0 0 85 95">
      <rect x="2" y="2" width="81" height="91" rx="9" fill="none" stroke="var(--ink)" stroke-width="4"/>
      <path d="M22 24 a28 28 0 0 1 41 0 M28 30 a19 19 0 0 1 29 0" fill="none" stroke="var(--ink)" stroke-width="4" stroke-linecap="round"/>
      <text x="42.5" y="62" text-anchor="middle" font-family="Montserrat, sans-serif" font-weight="700" font-size="30" fill="var(--ink)">4G</text>
      <text x="42.5" y="83" text-anchor="middle" font-family="Montserrat, sans-serif" font-weight="700" font-size="17" fill="var(--ink)">LTE</text>
    </svg>
  </section>

  <section class="feature" style="top:353px">
    <h2>Wifi Capable</h2>
    <p>Change screen content with a PC, tablet or mobile phone with an easy to use app</p>
    <svg class="feature-icon" viewBox="0 0 85 95">
      <rect x="2" y="2" width="81" height="91" rx="9" fill="none" stroke="var(--ink)" stroke-width="4"/>
      <path d="M16 30 a38 38 0 0 1 53 0 M24 39 a26 26 0 0 1 37 0 M32 48 a14 14 0 0 1 21 0" fill="none" stroke="var(--ink)" stroke-width="5" stroke-linecap="round"/>
      <circle cx="42.5" cy="56" r="5" fill="var(--ink)"/>
      <rect x="10" y="64" width="65" height="20" rx="3" fill="var(--ink)"/>
      <text x="42.5" y="79" text-anchor="middle" font-family="Montserrat, sans-serif" font-weight="700" font-size="13" fill="var(--paper)">Wi-Fi</text>
    </svg>
  </section>

  <section class="feature" style="top:505px">
    <h2>Intelligent Brightness</h2>
    <p>Screen will automatically adjust to suit ambiant light improving screen viewing quality and saving in power</p>
    <svg class="feature-icon" viewBox="0 0 85 95">
      <rect x="2" y="2" width="81" height="91" rx="9" fill="none" stroke="var(--ink)" stroke-width="4"/>
      <circle cx="42.5" cy="47.5" r="14" fill="none" stroke="var(--ink)" stroke-width="5"/>
      <path d="M42.5 33.5 a14 14 0 0 1 0 28 z" fill="var(--ink)"/>
      <g stroke="var(--ink)" stroke-width="6" stroke-linecap="round">
        <line x1="42.5" y1="15" x2="42.5" y2="19"/><line x1="42.5" y1="76" x2="42.5" y2="80"/>
        <line x1="10" y1="47.5" x2="14" y2="47.5"/><line x1="71" y1="47.5" x2="75" y2="47.5"/>
        <line x1="19.5" y1="24.5" x2="22.5" y2="27.5"/><line x1="62.5" y1="67.5" x2="65.5" y2="70.5"/>
        <line x1="65.5" y1="24.5" x2="62.5" y2="27.5"/><line x1="22.5" y1="67.5" x2="19.5" y2="70.5"/>
      </g>
    </svg>
  </section>

  <section class="feature" style="top:655px">
    <h2>Online Monitoring</h2>
    <p>Monitor cabinet temperature and humidity plus more in real time online.<br>Receive alerts via email.</p>
    <svg class="feature-icon" viewBox="0 0 85 95">
      <rect x="2" y="2" width="81" height="91" rx="9" fill="none" stroke="var(--ink)" stroke-width="4"/>
      <path d="M34 16 a8 8 0 0 1 16 0 v44 a15 15 0 1 1 -16 0 z" fill="none" stroke="var(--ink)" stroke-width="4"/>
      <line x1="42" y1="40" x2="42" y2="66" stroke="var(--ink)" stroke-width="4"/>
      <circle cx="42" cy="72" r="7" fill="var(--ink)"/>
      <g stroke="var(--ink)" stroke-width="3">
        <line x1="12" y1="16" x2="24" y2="16"/><line x1="12" y1="24" x2="22" y2="24"/>
        <line x1="12" y1="32" x2="24" y2="32"/><line x1="12" y1="40" x2="22" y2="40"/>
        <line x1="12" y1="48" x2="24" y2="48"/>
      </g>
      <path d="M62 30 q5 7 0 10 q-5 -3 0 -10 z M58 44 q5 7 0 10 q-5 -3 0 -10 z M68 44 q5 7 0 10 q-5 -3 0 -10 z" fill="var(--ink)"/>
      <text x="70" y="72" text-anchor="middle" font-family="Montserrat, sans-serif" font-weight="700" font-size="13" fill="var(--ink)">%</text>
    </svg>
  </section>

  <section class="feature" style="top:800px">
    <h2>High Quality Products</h2>
    <p>Setting high standard for colour, brightness and sharpness, these LED modules will create attention</p>
    <svg class="feature-icon" viewBox="0 0 85 95">
      <rect x="2" y="2" width="81" height="91" rx="9" fill="none" stroke="var(--ink)" stroke-width="4"/>
      <polygon points="42.5,20 49.5,38 68,39 53.5,51 58.5,70 42.5,59 26.5,70 31.5,51 17,39 35.5,38" fill="var(--ink)"/>
    </svg>
  </section>

  <div class="quote">
    <strong>1300 ZOFENWA</strong>
    <span>FOR A FREE QUOTE</span>
  </div>

  <div class="contact contact-web">WWW.ZOFENWA.COM.AU</div>
  <div class="contact contact-mail">INFO@ZOFENWA.COM.AU</div>
</main>
</body>
</html>
```